Business card design for Velluto Events, and Event & Entertainment business

The business card design is for a new business venture, Velluto Events. This company offers Event management, entertainment management and also Latin dance tuition. We currently run Latin dance festivals in Australia & also teach street Latin. This business card is for the director, Mara Dunhill. The Logo has already been designed. So, I need the new design to incorporate and go with the existing Logo.

The look I like is clean, simple & elegant but I also want it to be sexy. Elegant, but not corporate. Clean & simple but not boring :-)

If you want to add another design element as well as using the Logo, please use something with movement. I like ripples or swirls for example.

I would also like to have part of the card embossed or Spot UV pressed so I would like some part of the design to have texture.

Text for the Cards is as follows;

Velluto Events ( Logo attached )

Mara Dunhill

EVENTS & ENTERTAINMENT MANAGEMENT

m: 0478 352 601
e: mara@vellutoevents.com.au
f Velluto Events

www.vellutoevents.com.au

Please try portrait layout.

Thanks, Mara
Updates

Hello Designers, Thank you to all of you who have submitted designs for Velluto Events. I will make up my mind now from what I have already been sent. Very close to making a decision :-) Thank you, Mara

Target Market(s)

Adults, 18 - 60 age group. People who are active. People interested in different cultures. People who like to travel. Please who like to have fun. People who are passionate about Latin dance.

Industry/Entity Type

Entertainment

Font styles to use
Sans Serif
Script

Colors
9bcb3c
ec1f27
ffffff

Requirements
Must have
• Logo + All text listed in brief
Nice to have
• An extra design feature or background image that could be embossed or spot uv pressed to add texture & flare.

```html
<!DOCTYPE html>
<html lang="en">
<head>
<meta charset="utf-8">
<title>Velluto Events – Business Card</title>
<link rel="stylesheet" href="https://fonts.googleapis.com/css2?family=Open+Sans:wght@400;600&display=swap">
<style>
  :root {
    --stage: #1c1c1e;
    --card-blue: #b9dcf0;
    --ink: #231f20;
    --white: #ffffff;
    --orange: #e6641c;
    --red: #dc2126;
    --green: #86c12b;
    --accent-red: #9b2a2e;
  }
  * { box-sizing: border-box; margin: 0; padding: 0; }
  html, body {
    width: 1200px;
    height: 1100px;
    overflow: hidden;
    background: var(--stage);
    font-family: "Open Sans", Arial, sans-serif;
  }
  .stage {
    position: relative;
    width: 1200px;
    height: 1100px;
  }
  .card {
    position: absolute;
    top: 230px;
    width: 380px;
    height: 640px;
    overflow: hidden;
  }
  /* Front */
  .card-front {
    left: 170px;
    background: var(--card-blue);
  }
  .brand {
    position: absolute;
    left: 0;
    right: 0;
    display: flex;
    align-items: center;
    justify-content: center;
    gap: 12px;
  }
  .card-front .brand { top: 295px; }
  .brand-dot {
    width: 22px;
    height: 22px;
    border-radius: 50%;
    background: var(--accent-red);
    flex: none;
  }
  .brand-name {
    font-weight: 400;
    font-size: 34px;
    color: var(--ink);
    letter-spacing: 0.5px;
  }
  /* Back */
  .card-back { left: 650px; background: var(--white); }
  .card-back .backdrop { position: absolute; inset: 0; }
  .card-back .brand { top: 120px; }
  .tagline {
    position: absolute;
    top: 312px;
    left: 0; right: 0;
    text-align: center;
    color: var(--white);
    font-size: 19px;
    line-height: 1.3;
    text-transform: uppercase;
    letter-spacing: 0.3px;
  }
  .divider {
    position: absolute;
    top: 382px;
    left: 40px; right: 40px;
    height: 1px;
    background: var(--white);
  }
  .director {
    position: absolute;
    top: 396px;
    left: 0; right: 0;
    text-align: center;
    color: var(--white);
    font-size: 18px;
    font-weight: 600;
  }
  .contact {
    position: absolute;
    top: 428px;
    left: 0; right: 0;
    text-align: center;
    color: var(--white);
    font-size: 17px;
    line-height: 1.5;
    list-style: none;
  }
  .web {
    position: absolute;
    bottom: 0;
    left: 0; right: 0;
    height: 78px;
    display: flex;
    align-items: center;
    justify-content: center;
    color: var(--white);
    font-size: 18px;
  }
</style>
</head>
<body>
<main class="stage">
  <section class="card card-front" aria-label="Card front">
    <div class="brand">
      <span class="brand-dot"></span>
      <span class="brand-name">Velluto Events</span>
    </div>
  </section>

  <section class="card card-back" aria-label="Card back">
    <svg class="backdrop" width="380" height="640" viewBox="0 0 380 640" aria-hidden="true">
      <defs>
        <linearGradient id="heat" x1="0" y1="0" x2="1" y2="1">
          <stop offset="0" stop-color="#e8691b"/>
          <stop offset="1" stop-color="#d91f25"/>
        </linearGradient>
      </defs>
      <path d="M0 225 C 110 225, 230 270, 380 288 L380 640 L0 640 Z" fill="url(#heat)"/>
      <rect x="0" y="562" width="380" height="78" fill="#86c12b"/>
    </svg>
    <div class="brand">
      <span class="brand-dot"></span>
      <span class="brand-name">Velluto Events</span>
    </div>
    <p class="tagline">Events &amp; Entertainment<br>Management</p>
    <div class="divider"></div>
    <p class="director">Mara Dunhill</p>
    <ul class="contact">
      <li>m: 0478 352 601</li>
      <li>e: mara@vellutoevents.com.au</li>
      <li>f: Velluto Events</li>
    </ul>
    <p class="web">www.vellutoevents.com.au</p>
  </section>
</main>
</body>
</html>
```